Commercial Cleaning Company Needs A Flyer

We are a commercial cleaning company based in London.
We are currently trying to grow our client base and would like a fresh, professional flyer that differentiates us from the competition. We mainly specialises in commercial cleaning such as offices, educational facilities etc. I would like to see a flyer design that look professional, unique not cheap. I have attached a file that contains some company details but Im happy to explore other options if thay are relevant. Please also find company logo and colour chart, this should remain as is.

I have attached some pictures that contain diamond shaped windows. I feel that this can be used to represent and incorporate the logo. Please add to flyer where possible.

Please feel free to contact me for any further advice.
Thanks and good luck

Target Market(s)

commercial buildings and residential property owners

Industry/Entity Type

Cleaning Service

Contact Information for Business Card

Please refer to up loaded document for company details and logo colours.

Font styles to use
Sans Serif

Colors
33a6d7
33b8a4

Requirements
Must have
• Look Professional, not cheap, unique, stand out from others.

```html
<!DOCTYPE html>
<html lang="en">
<head>
<meta charset="utf-8">
<title>Brightway Office Care – Flyer and Business Cards</title>
<link href="https://fonts.googleapis.com/css2?family=Sorts+Mill+Goudy:ital@0;1&family=Open+Sans:wght@400;600;700&family=Montserrat:wght@700&display=swap" rel="stylesheet">
<style>
  :root{
    --brand-blue:#33a6d7;
    --brand-teal:#33b8a4;
    --panel-blue:#2a9bd0;
    --ink:#2b2b2b;
    --muted:#5a6b72;
    --card-pale:#e9eff2;
    --stage:#ececec;
    --white:#ffffff;
  }
  *{box-sizing:border-box;margin:0;padding:0}
  html,body{width:1200px;height:1000px;overflow:hidden;background:var(--stage)}
  .canvas{position:relative;width:1200px;height:1000px}

  /* ---------- name block ---------- */
  .brand{display:flex;align-items:center;gap:10px}
  .brand__dot{width:24px;height:24px;border-radius:50%;background:var(--brand-teal);flex:none}
  .brand__name{font:600 22px/1.1 'Open Sans',sans-serif;color:var(--brand-blue);white-space:nowrap}
  .brand__tag{font:400 13px/1.2 'Open Sans',sans-serif;color:var(--muted);margin-top:6px;white-space:nowrap}

  /* ---------- business cards ---------- */
  .card{position:absolute;left:45px;width:440px;height:250px;background:var(--white);box-shadow:0 2px 8px rgba(0,0,0,.15)}
  .card--front{top:200px;background:var(--card-pale);display:flex;flex-direction:column;align-items:center;justify-content:center}
  .card--front .brand__tag{margin-left:34px}
  .card--back{top:500px;padding:34px 26px}
  .card-back__row{display:flex;justify-content:space-between;align-items:flex-start}
  .card-back__brand .brand{gap:7px}
  .card-back__brand .brand__dot{width:16px;height:16px}
  .card-back__brand .brand__name{font-size:14px}
  .card-back__brand .brand__tag{font-size:10px;margin-left:23px;margin-top:4px}
  .card-contacts{list-style:none;font:400 11px/1.6 'Open Sans',sans-serif;color:#555;border-left:1px solid #ccc;padding-left:10px}
  .socials{display:flex;gap:5px;margin-top:4px}
  .socials span{width:13px;height:13px;border-radius:2px;background:var(--brand-blue)}
  .card-back__slogan{position:absolute;left:26px;bottom:34px;font:700 14px/1 'Montserrat',sans-serif;color:var(--brand-teal);white-space:nowrap}

  /* ---------- flyer ---------- */
  .flyer{position:absolute;left:543px;top:102px;width:632px;height:816px;background:var(--white);box-shadow:0 2px 10px rgba(0,0,0,.18);overflow:hidden}
  .flyer__stripe{position:absolute;left:0;top:440px;width:9px;bottom:0;background:var(--brand-blue)}
  .flyer__main{position:absolute;left:9px;top:0;width:345px;height:100%}
  .flyer__brand{position:absolute;left:26px;top:36px}
  .flyer__brand .brand__dot{width:28px;height:28px}
  .flyer__brand .brand__name{font-size:23px}
  .flyer__brand .brand__tag{font-size:14px;margin-left:38px}

  .about{position:absolute;left:26px;top:103px;width:304px;font:400 9.4px/1.32 'Sorts Mill Goudy',serif;color:var(--ink);text-align:justify}
  .about h2{font:italic 400 15px/1 'Sorts Mill Goudy',serif;color:var(--brand-teal);margin-bottom:5px}
  .about p{margin-bottom:10px}
  .about .about__promise{color:var(--brand-blue)}

  .quality{position:absolute;left:30px;top:299px;list-style:none;font:400 11.2px/1 'Sorts Mill Goudy',serif;color:var(--ink)}
  .quality li{display:flex;align-items:center;height:18.6px}
  .quality b{width:14px;height:14px;border-radius:50%;background:var(--brand-teal);color:var(--white);font:700 9px/14px 'Open Sans',sans-serif;text-align:center;margin-right:1px}

  .office-photo{position:absolute;left:0;top:440px;width:345px;height:376px;background:linear-gradient(180deg,#ffffff 0%,#e6eef2 25%,#b9c9d2 60%,#8a9aa4 100%)}
  .features{position:absolute;left:20px;top:455px;width:320px;display:flex;justify-content:space-between}
  .feature{width:76px;text-align:center;font:700 9.5px/1.05 'Montserrat',sans-serif;color:#1e1e1e;letter-spacing:.3px}
  .feature__icon{display:block;margin:0 auto 6px;width:50px;height:50px}

  .flyer__side{position:absolute;left:354px;top:0;width:278px;height:100%;background:var(--panel-blue);color:var(--white)}
  .side__headline{position:absolute;left:18px;top:30px;font:400 24px/1.28 'Sorts Mill Goudy',serif}
  .side__headline em{font-style:italic}
  .side__intro{position:absolute;left:18px;top:126px;width:230px;font:400 9px/1.25 'Sorts Mill Goudy',serif;color:#cfe8f5}

  .service{position:absolute;left:17px;width:250px}
  .service__head{display:flex;align-items:center;gap:10px;margin-bottom:6px}
  .service__icon{width:44px;height:44px;border-radius:50%;background:rgba(255,255,255,.9);flex:none}
  .service__title{font:700 11.5px/1 'Open Sans',sans-serif}
  .service__list{list-style:none;display:grid;grid-template-columns:128px 120px;font:600 8.4px/10.5px 'Open Sans',sans-serif}
  .service__list--single{grid-template-columns:1fr}
  .service__list li::before{content:"";display:inline-block;width:5px;height:5px;background:var(--white);transform:rotate(45deg);margin:0 6px 1px 2px}
  .service__list .in-second-column{grid-column:2}
  .service--commercial{top:166px}
  .service--services{top:270px}
  .service--residential{top:466px}
  .service--green{top:582px}

  .side__contact{position:absolute;left:17px;top:706px;width:250px;font:400 9.5px/1.3 'Sorts Mill Goudy',serif}
  .side__details{list-style:none;margin-top:14px;font:400 10.5px/15px 'Open Sans',sans-serif}
  .side__details li{display:flex;align-items:center;gap:5px}
  .side__socials{position:absolute;right:10px;top:42px;display:flex;gap:5px}
  .side__socials span{width:12px;height:12px;border-radius:2px;background:var(--white)}
</style>
</head>
<body>
<main class="canvas">

  <section class="card card--front" aria-label="Business card front">
    <div class="brand"><span class="brand__dot"></span><span class="brand__name">Brightway Office Care</span></div>
    <div class="brand__tag">Spotless spaces for busy teams</div>
  </section>

  <section class="card card--back" aria-label="Business card back">
    <div class="card-back__row">
      <div class="card-back__brand">
        <div class="brand"><span class="brand__dot"></span><span class="brand__name">Brightway Office Care</span></div>
        <div class="brand__tag">Spotless spaces for busy teams</div>
      </div>
      <ul class="card-contacts">
        <li>07700 900123</li>
        <li>020 7946 0321</li>
        <li>hello@brightwayofficecare.com</li>
        <li>brightwayofficecare.com</li>
        <li class="socials"><span></span><span></span><span></span><span></span></li>
      </ul>
    </div>
    <p class="card-back__slogan">We're making London brighter - one office at a time</p>
  </section>

  <article class="flyer">
    <div class="flyer__main">
      <div class="flyer__brand">
        <div class="brand"><span class="brand__dot"></span><span class="brand__name">Brightway Office Care</span></div>
        <div class="brand__tag">Spotless spaces for busy teams</div>
      </div>

      <section class="about">
        <h2>About Us</h2>
        <p>Brightway Office Care continual commitment and dedication to delivering a quality service has enabled us to build a solid foundation within the cleaning industry. Our principle and objectives are simple, provide our customers with an affordable quality service to suit their needs and always put our clients first.</p>
        <p>BOC rewards dependability, integrality and provide the training and development for all employees to achieve the best possible results. We believe that building relationships based on ethical conduct towards employees and clientele defines our unique working environments and is a vital key to our success.</p>
        <p class="about__promise">This is why at Brightway Office Care stand behind our performance and guarantee your satisfaction.</p>
      </section>

      <ul class="quality">
        <li><b>Q</b>uick response to costumers needs guaranteed</li>
        <li><b>U</b>nequal attention to detail</li>
        <li><b>A</b>ffordable cleaning tailored to your needs</li>
        <li><b>L</b>engthy industry experience</li>
        <li><b>I</b>nsurance inclusive of workers compensation and liability</li>
        <li><b>T</b>raining provided to all staff and supervisors</li>
        <li><b>Y</b>our satisfaction is our priority</li>
      </ul>

      <div class="office-photo" role="img" aria-label="Photo of a bright, clean open-plan office with desk, chairs and large windows"></div>

      <div class="features">
        <div class="feature">
          <svg class="feature__icon" viewBox="0 0 50 50" aria-hidden="true"><circle cx="25" cy="25" r="25" fill="var(--brand-teal)"/><circle cx="25" cy="23" r="7" fill="none" stroke="#fff" stroke-width="2"/><rect x="22" y="30" width="6" height="5" fill="#fff"/><path d="M25 9v4M13 22h-4M41 22h-4M16 14l2.5 2.5M34 14l-2.5 2.5" stroke="#fff" stroke-width="2"/></svg>
          SPARKLING<br>SERVICE
        </div>
        <div class="feature">
          <svg class="feature__icon" viewBox="0 0 50 50" aria-hidden="true"><circle cx="25" cy="25" r="25" fill="var(--brand-teal)"/><path d="M25 37 12 24a7 7 0 0 1 13-8 7 7 0 0 1 13 8z" fill="#fff"/></svg>
          QUALITY<br>CLEANERS
        </div>
        <div class="feature">
          <svg class="feature__icon" viewBox="0 0 50 50" aria-hidden="true"><circle cx="25" cy="25" r="25" fill="var(--brand-teal)"/><circle cx="25" cy="24" r="6" fill="none" stroke="#fff" stroke-width="2"/><rect x="22.5" y="30" width="5" height="5" fill="#fff"/><path d="M25 11v4M14 24h-3M39 24h-3" stroke="#fff" stroke-width="2"/></svg>
          HUMAN<br>SUPPORT
        </div>
        <div class="feature">
          <svg class="feature__icon" viewBox="0 0 50 50" aria-hidden="true"><circle cx="25" cy="25" r="25" fill="var(--brand-teal)"/><path d="M22 16v16a4 4 0 0 0 8 0V13a3 3 0 0 0-6 0v18" fill="none" stroke="#fff" stroke-width="2.4" stroke-linecap="round"/></svg>
          COMPETITIVE<br>PRICING
        </div>
      </div>
    </div>
    <div class="flyer__stripe"></div>

    <aside class="flyer__side">
      <h1 class="side__headline">Sparkling Service.<br>Attention to Detail.<br><em>Human Support.</em></h1>
      <p class="side__intro">We aim to offer the highest Commercial and Residential cleaning standards.</p>

      <section class="service service--commercial">
        <div class="service__head"><span class="service__icon" role="img" aria-label="Vacuum cleaner icon"></span><h3 class="service__title">Commercial Cleaning</h3></div>
        <ul class="service__list"><li>Offices</li><li>Restaurants</li><li>Education Facilities</li><li>Showroom</li><li>Medical Facilities</li></ul>
      </section>

      <section class="service service--services">
        <div class="service__head"><span class="service__icon" role="img" aria-label="Two people shaking hands icon"></span><h3 class="service__title">Services</h3></div>
        <ul class="service__list service__list--single">
          <li>General Cleaning Requirements</li><li>Consumables supply and replacement</li><li>Washroom services</li><li>Building maintenance</li><li>Window cleaning</li><li>Carpet care</li><li>Floor maintenance</li><li>Scrubbing machinery</li><li>PAT Testing</li><li>Waste removal</li><li>Recycling Programs</li>
        </ul>
      </section>

      <section class="service service--residential">
        <div class="service__head"><span class="service__icon" role="img" aria-label="House with cleaning tools icon"></span><h3 class="service__title">Residential Cleaning</h3></div>
        <ul class="service__list"><li>House Cleaning</li><li>After Event Cleaning</li><li>Apartment Cleaning</li><li>Spring Cleaning</li><li>Move In/Out Cleaning</li><li>Post Building Works</li><li class="in-second-column">Deep Clean</li></ul>
      </section>

      <section class="service service--green">
        <div class="service__head"><span class="service__icon" role="img" aria-label="House with leaf icon"></span><h3 class="service__title">Green Cleaning Available</h3></div>
        <ul class="service__list"><li>No harmful chemicals</li><li>Eco-friendly</li><li>Safe for children and pets</li><li>No artificial fragrances</li></ul>
      </section>

      <section class="side__contact">
        <p>Would you like your office building assessed? We'll visit, give you a quote.... Contact Us at</p>
        <div class="side__socials"><span></span><span></span><span></span><span></span></div>
        <ul class="side__details">
          <li><svg width="9" height="11" viewBox="0 0 9 11" aria-hidden="true"><rect x=".8" y=".8" width="7.4" height="9.4" rx="1.2" fill="none" stroke="#fff" stroke-width="1.1"/></svg>07700 900123</li>
          <li><svg width="9" height="11" viewBox="0 0 9 11" aria-hidden="true"><path d="M4.5 10S1 6 1 4a3.5 3.5 0 0 1 7 0c0 2-3.5 6-3.5 6z" fill="none" stroke="#fff" stroke-width="1.1"/></svg>020 7946 0321</li>
          <li><svg width="10" height="9" viewBox="0 0 10 9" aria-hidden="true"><rect x=".6" y="1" width="8.8" height="6.6" fill="none" stroke="#fff" stroke-width="1"/><path d="M.6 1 5 5l4.4-4" fill="none" stroke="#fff" stroke-width="1"/></svg>hello@brightwayofficecare.com</li>
          <li><svg width="10" height="10" viewBox="0 0 10 10" aria-hidden="true"><circle cx="5" cy="5" r="4.2" fill="none" stroke="#fff" stroke-width="1"/><path d="M.8 5h8.4M5 .8c2 2.5 2 5.9 0 8.4M5 .8c-2 2.5-2 5.9 0 8.4" fill="none" stroke="#fff" stroke-width=".8"/></svg>brightwayofficecare.com</li>
        </ul>
      </section>
    </aside>
  </article>

</main>
</body>
</html>
```